Updated Business Card Re-design (Logo Provided)

I am needing to update our business cards for our practice, Bright Care Partners. We are a personal injury and wellness practice. The final design should be elegant and classy, but a type of card people would want to keep. Any samples should only have Dr. Tomas Verlinde on the template.
Updates

Went on vacation/holiday

Need extra days to review

Target Market(s)

Personal Injury clients, wellness clients

Industry/Entity Type

Personal Injury, medical, wellness

Contact Information for Business Card

dr and practice name, offerings

Requirements
Must have
• Single sided, this will be printed on a transparent business card, no exceptions.

```html
<!DOCTYPE html>
<html lang="en">
<head>
<meta charset="utf-8">
<title>Bright Care Partners – Business Card</title>
<link href="https://fonts.googleapis.com/css2?family=Lato:wght@400;700;900&display=swap" rel="stylesheet">
<style>
  :root {
    --page: #e4e0da;
    --card: #f4f4f3;
    --blue: #1d6aa8;
    --blue-dark: #1f5f8f;
    --orange: #d88a2c;
    --green: #3a8a4e;
    --text: #3c3c3c;
    --white: #ffffff;
  }
  * { margin: 0; padding: 0; box-sizing: border-box; }
  html, body {
    width: 1200px; height: 900px; overflow: hidden;
    background: var(--page);
    font-family: "Lato", sans-serif;
  }
  .card {
    position: absolute; left: 160px; top: 197px;
    width: 880px; height: 506px;
    background: var(--card);
    border-radius: 18px;
    overflow: hidden;
    box-shadow: 0 10px 30px rgba(0,0,0,0.12);
  }
  .brand {
    position: absolute; right: 58px; top: 92px;
    display: flex; align-items: center; gap: 16px;
  }
  .brand-dot {
    width: 46px; height: 46px; border-radius: 50%;
    background: var(--orange);
  }
  .brand-name {
    color: var(--blue);
    font-weight: 900; font-size: 30px; line-height: 1.05;
    letter-spacing: -0.5px; text-transform: uppercase; text-align: right;
  }
  .doctor-name {
    position: absolute; left: 50px; top: 236px;
    color: var(--blue-dark);
    font-weight: 900; font-size: 31px; letter-spacing: 0.3px;
  }
  .specialty {
    position: absolute; left: 50px; top: 275px;
    color: var(--orange); font-weight: 700; font-size: 19px;
  }
  .divider {
    position: absolute; left: 50px; right: 64px; top: 314px;
    height: 2px; background: var(--green);
  }
  .contacts {
    position: absolute; left: 50px; top: 336px;
    list-style: none; color: var(--text); font-size: 19px;
  }
  .contacts li {
    display: flex; align-items: center; gap: 12px; height: 31px;
  }
  .contacts svg { width: 16px; height: 16px; fill: var(--blue-dark); }
  .address {
    position: absolute; right: 58px; top: 336px;
    text-align: right; font-size: 19px; color: var(--text); line-height: 31px;
  }
  .address .practice { color: var(--blue); }
  .footer-green {
    position: absolute; left: 0; top: 480px;
    width: 540px; height: 24px; background: var(--green);
  }
  .footer-blue {
    position: absolute; right: 0; top: 458px; bottom: 0;
    width: 366px; background: var(--blue);
    border-top-left-radius: 24px;
    display: flex; align-items: center; justify-content: flex-end;
    padding-right: 40px;
    color: var(--white); font-size: 16.5px; letter-spacing: 0.2px;
    white-space: nowrap;
  }
  .footer-blue b { font-weight: 900; }
  .footer-mark {
    position: absolute; left: 462px; top: 464px;
    width: 34px; height: 34px; border-radius: 50%;
    background: var(--orange);
  }
</style>
</head>
<body>
  <div class="card">
    <div class="brand">
      <span class="brand-dot"></span>
      <div class="brand-name">Bright Care<br>Partners</div>
    </div>

    <h1 class="doctor-name">DR. TOMAS VERLINDE, D.C.</h1>
    <p class="specialty">Medical-PT-Chiropractic</p>
    <div class="divider"></div>

    <ul class="contacts">
      <li>
        <svg viewBox="0 0 24 24"><path d="M6.6 10.8a15.1 15.1 0 0 0 6.6 6.6l2.2-2.2a1 1 0 0 1 1-.25 11.4 11.4 0 0 0 3.6.57 1 1 0 0 1 1 1V20a1 1 0 0 1-1 1A17 17 0 0 1 3 4a1 1 0 0 1 1-1h3.5a1 1 0 0 1 1 1c0 1.25.2 2.45.57 3.57a1 1 0 0 1-.25 1z"/></svg>
        555.214.7380
      </li>
      <li>
        <svg viewBox="0 0 24 24"><path d="M7 1h10a2 2 0 0 1 2 2v18a2 2 0 0 1-2 2H7a2 2 0 0 1-2-2V3a2 2 0 0 1 2-2zm0 3v14h10V4zm5 15.2a1.2 1.2 0 1 0 0 2.4 1.2 1.2 0 0 0 0-2.4z"/></svg>
        555.318.6042
      </li>
      <li>
        <svg viewBox="0 0 24 24"><path d="M2 5h20v14H2zm2 2v.5l8 5 8-5V7zm0 2.8V17h16V9.8l-8 5z"/></svg>
        hello@brightcarepartners.com
      </li>
    </ul>

    <div class="address">
      <div class="practice">Bright Care Partners</div>
      <div>4820 Orchard Lane, Suite 12</div>
      <div>Fairview, GA 30999</div>
    </div>

    <div class="footer-green"></div>
    <div class="footer-blue">WWW.<b>BRIGHTCAREPARTNERS</b>.COM</div>
    <span class="footer-mark"></span>
  </div>
</body>
</html>
```